Packaging design pot 500gr Polynesian honey

Task Description

Concept of design:

"This Polynesian island is a small piece of paradise nestled in the South Pacific, away from any form of civilization ( ideal place for producing honey of excellence )
= Images / symbols that induces dreaming)); (100% organic, 100% natural organic Honey logo)
Elegant, subtle , eyes catching, NO pictures of bees , Simple colors: BLACK, GOLD, WHITE, tranparency . (Designer discretion)
(Bio label optional )

the Labels: Hex1 product of TAHITI header: LOVAHINE HONEY (brand name) MAY USE all images herein below , free of copyright (Macro coconut flower, coconut white sand beach, exoticism; 500 gr; text on back (see attached text); Position the bar code vertically on the back; Mandatory address: Website on the back, infocontact, registration number.

500g pot :
HEIGHT With cap 12.00cm Without cap 11.85 cm
outside diameter 7.24cm
Label height should only be = 5, 1 cm x height
See the container with black cap.

Deadline
March 15, 2018 ( postpone if needed )
Updates

To all participants, i have added a personal photo you may want to consider in your creative process. If the upper section of the photo is exploited, I thought it has something interesting to bring: blue sky on the background including a shadow ot the coconut leaves, ( no bees please).

Finally i have added the colour of Lovahine Honey

Dear participants, I have updated two files to be taken into account onward : 1) final text: in French ; the replicate is English for the English version valid with the identical Graphic design 2) the true colours of Lovahine Honey, for your consideration. I thought that with the help of day light i could enhance its true body colour. Best regards, Mr KOL

Target Market(s)

Target the Asian market , Onward The US MARKET, (LUXURY oriented)

Font styles to use
Serif

Colors

Designer to choose colors to be used in the design.

Requirements
Must have
• Website address on the back, infocontact, registration number,
• texte ( summary )
• coconut tree honey ( ORIGIN )
• Color code : BLACK , GOLD , light , transparency
• COLORS THAT MATCH COLOR OF THE HONEY : DARK RED AMBER SEE IMAGE ATTACHED
Nice to have
• A matching logo
• A 400g Squezze bottle format ;
• h18.5*d7.8*c3.2(cm)
Should not have
• No Bees

```html
<!DOCTYPE html>
<html lang="fr">
<head>
<meta charset="utf-8">
<title>Lovahine Honey – Étiquette pot 500 g</title>
<link rel="stylesheet" href="https://fonts.googleapis.com/css2?family=Playfair+Display:wght@400;700&family=Montserrat:wght@700&display=swap">
<style>
  :root {
    --black: #141414;
    --black-soft: #1f1f1f;
    --gold: #c9a64a;
    --gold-light: #f2dc8a;
    --gold-dark: #7a5d1c;
    --white: #ffffff;
    --text-light: #e9e6df;
    --serif: "Playfair Display", Georgia, serif;
    --sans: "Montserrat", Arial, sans-serif;
  }
  * { box-sizing: border-box; margin: 0; padding: 0; }
  html, body { width: 1200px; height: 1200px; overflow: hidden; background: var(--white); }
  .canvas { position: relative; width: 1200px; height: 1200px; }

  /* Main wrap label */
  .label-main {
    position: absolute; left: 22px; top: 19px; width: 1157px; height: 275px;
    background: var(--black); color: var(--text-light); font-family: var(--serif);
    overflow: hidden;
  }
  .label-main__goldband {
    position: absolute; left: 0; top: 0; width: 100%; height: 22px;
    background: linear-gradient(90deg, var(--gold-light) 0%, var(--gold) 35%, var(--gold-dark) 60%, var(--gold) 85%, var(--gold-light) 100%);
  }
  .label-main__pattern {
    position: absolute; left: 300px; top: 160px; width: 620px; height: 115px;
    background: linear-gradient(180deg, #262219 0%, #3a3121 60%, #2a2418 100%);
  }

  /* Left panel: nutrition facts */
  .facts__rule { position: absolute; left: 16px; width: 396px; height: 1px; background: var(--gold); }
  .facts__rule--top { top: 31px; }
  .facts__rule--bottom { top: 192px; }
  .facts__title { position: absolute; left: 28px; top: 36px; font-size: 9.6px; font-weight: 700; line-height: 13px; white-space: nowrap; }
  .facts__heading { position: absolute; left: 32px; top: 73px; font-size: 9.6px; font-weight: 700; line-height: 11px; white-space: nowrap; }
  .facts__col { position: absolute; font-size: 9.6px; line-height: 10px; text-align: center; }
  .facts__col--100 { left: 200px; top: 104px; width: 54px; }
  .facts__col--portion { left: 262px; top: 104px; width: 100px; white-space: nowrap; }
  .facts__col--daily { left: 358px; top: 74px; width: 66px; }
  .facts__row { position: absolute; left: 24px; width: 400px; height: 14px; font-size: 9.6px; line-height: 10px; }
  .facts__row span { position: absolute; top: 0; text-align: center; }
  .facts__row .facts__name { left: 0; text-align: left; white-space: nowrap; }
  .facts__row .v100 { left: 176px; width: 54px; }
  .facts__row .vportion { left: 238px; width: 100px; }
  .facts__row .vdaily { left: 334px; width: 66px; white-space: nowrap; }
  .facts__row--energy { top: 126px; }
  .facts__row--protein { top: 151px; }
  .facts__row--carbs { top: 165px; }
  .facts__row--fat { top: 179px; }
  .facts__info { position: absolute; left: 24px; top: 197px; width: 300px; font-size: 9.6px; line-height: 10.4px; }
  .facts__info .indent { padding-left: 88px; }

  /* Center panel: brand */
  .brand { position: absolute; left: 429px; top: 27px; width: 310px; text-align: center; }
  .brand__name { font-size: 27px; font-weight: 700; color: var(--white); line-height: 30px; }
  .brand__variety { font-size: 15px; color: var(--white); line-height: 16px; margin-top: -2px; }
  .brand__organic { position: absolute; left: 196px; top: 64px; font-size: 12px; font-weight: 700; color: var(--gold); }
  .brand__mark { display: flex; align-items: center; justify-content: center; gap: 8px; margin-top: 30px; height: 56px; }
  .brand__mark-dot { width: 12px; height: 12px; border-radius: 50%; background: var(--white); }
  .brand__mark-name { font-size: 26px; font-weight: 700; color: var(--white); }
  .brand__tagline { font-family: var(--sans); font-size: 13.5px; letter-spacing: 3.5px; color: var(--white); margin-top: 12px; }
  .brand__origin { font-family: var(--sans); font-size: 21px; letter-spacing: 2px; color: var(--gold); margin-top: 4px; }
  .brand__circle { width: 20px; height: 20px; border-radius: 50%; border: 4px solid var(--gold-light); margin: 6px auto 0; }

  /* Right panel: story */
  .story { position: absolute; left: 728px; top: 36px; width: 398px; font-size: 9.6px; line-height: 10.4px; color: var(--text-light); }
  .story__title { font-weight: 700; }
  .story__best-before { position: absolute; left: 728px; top: 234px; font-size: 9.6px; color: var(--text-light); }
  .label-main__code-area { position: absolute; left: 1036px; top: 232px; width: 86px; height: 43px; background: var(--white); }

  /* Seal strip */
  .seal {
    position: absolute; left: 20px; top: 356px; width: 562px; height: 50px;
    background: linear-gradient(90deg, var(--gold-dark) 0%, var(--gold-light) 20%, var(--gold) 45%, #3d2f12 70%, var(--black) 72%);
  }
  .seal__pattern { position: absolute; right: 0; top: 0; width: 154px; height: 50px; background: linear-gradient(180deg, #3a3121, #262219); }
  .seal__hex {
    position: absolute; left: 36px; top: -10px; width: 64px; height: 72px;
    background: var(--black-soft);
    clip-path: polygon(50% 0, 100% 25%, 100% 75%, 50% 100%, 0 75%, 0 25%);
  }
  .seal__hex-fill { position: absolute; left: 20px; top: 24px; width: 24px; height: 22px; border-radius: 4px; background: #e39a23; }
  .seal__name { position: absolute; left: 120px; top: 6px; font-family: var(--serif); font-weight: 700; font-size: 20px; color: var(--black); }
  .seal__place { position: absolute; left: 120px; top: 30px; font-family: var(--serif); font-weight: 700; font-size: 12px; color: var(--black); }
</style>
</head>
<body>
<main class="canvas">

  <section class="label-main" aria-label="Étiquette principale du pot 500 g">
    <div class="label-main__goldband"></div>
    <div class="label-main__pattern" role="img" aria-label="Motif décoratif doré répété sur fond noir"></div>

    <div class="facts__rule facts__rule--top"></div>
    <p class="facts__title">Miel 100% BIO et 100 % naturel de l'atoll de Lovahine 500 gr<br>100% Organic Honey &amp; 100% natural from the Island of Lovahine</p>
    <p class="facts__heading">NUTRITIVE FACTS<br>VALEURS NUTRITIONNELLES MOYENNES</p>
    <p class="facts__col facts__col--100">100 gr</p>
    <p class="facts__col facts__col--portion">Per portion 10 gr</p>
    <p class="facts__col facts__col--daily">% Daily<br>value Valeur<br>Qutidienne<br>pour/ per<br>10gr</p>
    <div class="facts__row facts__row--energy"><span class="facts__name">Energy value/Valeur énergétique</span><span class="v100">1365Kj<br>321 Kcal</span><span class="vportion">136Kj<br>32 Kcal</span><span class="vdaily">2 Kj &nbsp;1 Kcal</span></div>
    <div class="facts__row facts__row--protein"><span class="facts__name">Protein/ Protéines &nbsp;gr</span><span class="v100">0,4</span><span class="vportion">0,04</span><span class="vdaily">&lt; 1</span></div>
    <div class="facts__row facts__row--carbs"><span class="facts__name">Carbohydrates/Glucides gr</span><span class="v100">80</span><span class="vportion">8</span><span class="vdaily">3</span></div>
    <div class="facts__row facts__row--fat"><span class="facts__name">Fat / Lipides &nbsp;gr</span><span class="v100">0</span><span class="vportion">0</span><span class="vdaily">0</span></div>
    <div class="facts__rule facts__rule--bottom"></div>
    <p class="facts__info">
      Conserver à moins de 21° dans un endroit frais et sec. Ne pas utiliser si le bouchon est cassé.<br>
      Lovahine Sud Island PO Box 1180, PAPEETE TAHITI 98700<br>
      FRENCH POLYNESIA<br>
      lovahinehoney.com info@lovahinehoney.com<br>
      <span class="indent">Miel Honey Honig عسل 蜂蜜</span>
    </p>

    <div class="brand">
      <h1 class="brand__name">Lovahine Honey</h1>
      <p class="brand__variety">Cocotier</p>
      <p class="brand__organic">100% Organic</p>
      <div class="brand__mark">
        <span class="brand__mark-dot"></span>
        <span class="brand__mark-name">Lovahine</span>
      </div>
      <p class="brand__tagline">Miel de Fluers</p>
      <p class="brand__origin">Tahiti</p>
      <div class="brand__circle"></div>
    </div>

    <div class="story">
      <p><span class="story__title">Miel de Lovahine</span><br>
      Situé sur l'atoll privé de Lovahine, le Rucher de Lovahine Honey offre un cadre de vie privilégié à ses abeilles. Cette île polynésienne est un petit bout de paradis lové dans le Pacifique Sud, à l'écart de toute forme de civilisation. Ses paysages luxuriants, sa plage de sable blanc sur fond de cocoteraies et ses eaux cristallines en font un havre de paix propice à la production d'un miel d'excellence. Cette terre volcanique très peu peuplée est totalement préservée de la pollution humaine, permettant aux abeilles de butiner dans un environnement sain. Accessible seulement par jet privé, l'île de Lovahine semble vivre hors du temps. La surface de terres émergées s'étire sur 14 km2, ce qui fait de son miel mille-fleurs un aliment naturel pur et rare. Les fleurs poussent à l'état sauvage et les pesticides n'existent pas. Ici, les apiculteurs prennent le temps de parler à leurs abeilles et travaillent dans le respect de la nature. Grâce à sa très grande qualité et sa récolte régulière, ce véritable produit de luxe s'est forgé une réputation de bouche à oreille dans tout le Pacifique. Les abeilles recueillent principalement le nectar de fleurs de cocotiers certifiés BIO, sans pesticides. Riche en parfum, ce produit d'exception provient exclusivement des îles vierges de l'archipel des Gambier. Il ne contient ni colorant, ni conservateur.<br>
      Ingrédients : Miel de Lovahine.</p>
    </div>
    <p class="story__best-before">A consommer avant : lire sur l'emballage</p>
    <div class="label-main__code-area"></div>
  </section>

  <section class="seal" aria-label="Bande de scellé du couvercle">
    <div class="seal__pattern" role="img" aria-label="Motif décoratif doré répété sur fond noir"></div>
    <div class="seal__hex">
      <div class="seal__hex-fill" role="img" aria-label="Emplacement de l'illustration centrale du médaillon"></div>
    </div>
    <p class="seal__name">Lovahine Honey</p>
    <p class="seal__place">tahiti</p>
  </section>

</main>
</body>
</html>
```